Business Card Design Project

I have attached the logo and the colour pallete for the branding for the company.

Creative designs for business cards are needed.

The Company is modern corporate.

Industry/Entity Type

Business

```html
<!DOCTYPE html>
<html lang="en">
<head>
<meta charset="utf-8">
<title>Northvale business card concepts</title>
<link href="https://fonts.googleapis.com/css2?family=Mulish:wght@400;600;700&display=swap" rel="stylesheet">
<style>
  :root {
    --plum: #6e2a63;
    --plum-deep: #4b2346;
    --plum-bright: #7d2c70;
    --orange: #ec5a1c;
    --amber: #f28c1e;
    --peach: #f6c08c;
    --ink: #2b2b2b;
    --grey: #555;
    --board: #d9d9d9;
    --paper: #ffffff;
  }
  * { box-sizing: border-box; margin: 0; padding: 0; }
  html, body { width: 1200px; height: 709px; overflow: hidden; }
  body {
    background: var(--board);
    font-family: "Mulish", Arial, sans-serif;
    color: var(--ink);
    position: relative;
  }
  .concept-number {
    position: absolute;
    font-size: 22px;
    color: #333;
  }
  .card {
    position: absolute;
    width: 520px;
    height: 289px;
    background: var(--paper);
    overflow: hidden;
    box-shadow: 0 2px 6px rgba(0,0,0,.25);
  }
  .card > * { position: absolute; }
  .wordmark {
    font-weight: 600;
    letter-spacing: -1px;
    color: var(--plum);
    line-height: 1;
    white-space: nowrap;
  }
  .holder-name { font-weight: 700; font-size: 15px; line-height: 1.2; }
  .holder-role { font-size: 14px; color: var(--grey); line-height: 1.2; }
  .contact-list { list-style: none; font-size: 14px; line-height: 23px; }
  .contact-list li { display: flex; align-items: center; gap: 4px; white-space: nowrap; }
  .ico { width: 11px; height: 11px; flex: none; }
  .ico-plum { color: var(--plum); }
  .ico-orange { color: var(--orange); }
  .address { font-size: 11.5px; line-height: 15px; color: var(--ink); }
  .art { left: 0; top: 0; }

  /* Card 1 */
  .card-gradient {
    left: 52px; top: 36px; width: 519px; height: 289px;
    background: linear-gradient(90deg, var(--plum-deep) 0%, #6a4a6a 6%, #d9cfe0 14%, #ffffff 30%, #fde6cf 42%, var(--peach) 60%, #f08a45 82%, var(--orange) 100%);
  }
  .card-gradient .wordmark { left: 74px; top: 40px; font-size: 46px; color: var(--ink); }
  .card-gradient .identity { right: 358px; top: 148px; text-align: right; }
  .card-gradient .divider {
    left: 169px; top: 82px; width: 3px; height: 182px;
    background: linear-gradient(180deg, var(--orange), #f3a36b 60%, rgba(255,255,255,.4));
  }
  .card-gradient .contact-list { left: 188px; top: 127px; line-height: 18px; font-size: 14px; }
  .card-gradient .address { left: 207px; top: 210px; }

  /* Card 2 */
  .card-wave { left: 620px; top: 36px; width: 521px; }
  .card-wave .wordmark { left: 34px; top: 64px; font-size: 50px; }
  .card-wave .identity { left: 126px; top: 142px; width: 0; display: flex; flex-direction: column; align-items: center; }
  .card-wave .identity > * { white-space: nowrap; }
  .card-wave .address { left: 291px; top: 56px; }
  .card-wave .contact-list { left: 288px; top: 127px; }
  .card-wave .site { left: 0; width: 521px; top: 259px; text-align: center; color: #fff; font-weight: 700; font-size: 14px; }

  /* Card 3 */
  .card-diagonal { left: 52px; top: 363px; width: 521px; height: 292px; }
  .card-diagonal .tilted { transform: rotate(-20deg); transform-origin: left top; }
  .card-diagonal .wordmark { left: 8px; top: 144px; font-size: 36px; }
  .card-diagonal .identity { left: 225px; top: 82px; color: #fff; }
  .card-diagonal .identity .holder-name { font-size: 22px; }
  .card-diagonal .identity .holder-role { font-size: 22px; color: #fff; }
  .card-diagonal .contact-list { left: 255px; top: 166px; font-size: 14px; line-height: 19px; }
  .card-diagonal .address { left: 282px; top: 238px; font-size: 13px; line-height: 17px; }

  /* Card 4 */
  .card-band { left: 619px; top: 363px; width: 520px; }
  .card-band .identity { left: 57px; top: 71px; }
  .card-band .contact-list { left: 41px; top: 129px; }
  .card-band .wordmark { left: 268px; top: 50px; font-size: 48px; }
  .card-band .address { left: 272px; top: 147px; }
  .card-band .site { left: 57px; top: 257px; color: #fff; font-weight: 700; font-size: 14px; }
</style>
</head>
<body>

<svg width="0" height="0" style="position:absolute" aria-hidden="true">
  <defs>
    <symbol id="i-phone" viewBox="0 0 12 12"><path fill="currentColor" d="M2.5 1h2l1 2.6-1.3 1a6.5 6.5 0 0 0 3.2 3.2l1-1.3 2.6 1v2a1 1 0 0 1-1 1A9.5 9.5 0 0 1 1.5 2a1 1 0 0 1 1-1z"/></symbol>
    <symbol id="i-mobile" viewBox="0 0 12 12"><rect x="2.5" y="0.8" width="7" height="10.4" rx="1" fill="none" stroke="currentColor" stroke-width="1.2"/><rect x="5" y="9" width="2" height="1" fill="currentColor"/></symbol>
    <symbol id="i-mail" viewBox="0 0 12 12"><rect x="0.8" y="2.5" width="10.4" height="7" fill="currentColor"/><path d="M1 3l5 3.5L11 3" fill="none" stroke="#fff" stroke-width="1"/></symbol>
    <symbol id="i-web" viewBox="0 0 12 12"><circle cx="6" cy="6" r="5" fill="currentColor"/><path d="M1 6h10M6 1c-2.5 3-2.5 7 0 10M6 1c2.5 3 2.5 7 0 10" fill="none" stroke="#fff" stroke-width=".8"/></symbol>
  </defs>
</svg>

<span class="concept-number" style="left:20px;top:44px">1</span>
<span class="concept-number" style="left:582px;top:38px">2</span>
<span class="concept-number" style="left:20px;top:372px">3</span>
<span class="concept-number" style="left:598px;top:376px">4</span>

<section class="card card-gradient">
  <div class="wordmark">northvale</div>
  <div class="identity">
    <p class="holder-name">Your Name</p>
    <p class="holder-role">Position</p>
  </div>
  <div class="divider"></div>
  <ul class="contact-list">
    <li><svg class="ico ico-orange"><use href="#i-phone"/></svg>123-456-7890</li>
    <li><svg class="ico ico-orange"><use href="#i-mobile"/></svg>123-456-7888</li>
    <li><svg class="ico ico-orange"><use href="#i-mail"/></svg>hello@northvale.com</li>
    <li><svg class="ico ico-orange"><use href="#i-web"/></svg>www.northvale.com</li>
  </ul>
  <p class="address">Address: 4170 W. Harbor Lane.<br>Suite 310<br>Dayton, OH 45402</p>
</section>

<section class="card card-wave">
  <svg class="art" width="521" height="289" viewBox="0 0 521 289">
    <defs>
      <linearGradient id="wave-plum" x1="0" x2="1"><stop offset="0" stop-color="#4b2346"/><stop offset="1" stop-color="#7d2c70"/></linearGradient>
    </defs>
    <path d="M0 212 C60 230 110 252 190 246 C300 238 380 212 521 220 L521 289 L0 289Z" fill="url(#wave-plum)"/>
    <path d="M0 212 C50 224 120 242 170 244 C110 246 50 236 0 224Z" fill="var(--orange)"/>
    <path d="M360 216 C420 210 480 212 521 220 L521 230 C480 222 420 218 360 216Z" fill="var(--orange)"/>
  </svg>
  <div class="wordmark">northvale</div>
  <div class="identity">
    <p class="holder-name">Your Name</p>
    <p class="holder-role">Position</p>
  </div>
  <p class="address">Address: 4170 W. Harbor Lane.<br>Suite 310<br>Dayton, OH 45402</p>
  <ul class="contact-list">
    <li><svg class="ico ico-plum"><use href="#i-mobile"/></svg>123-456-7890</li>
    <li><svg class="ico ico-plum"><use href="#i-phone"/></svg>123-456-7888</li>
    <li><svg class="ico ico-plum"><use href="#i-mail"/></svg>hello@northvale.com</li>
  </ul>
  <p class="site">www.northvale.com</p>
</section>

<section class="card card-diagonal">
  <svg class="art" width="521" height="292" viewBox="0 0 521 292">
    <defs>
      <linearGradient id="diag-orange" x1="0" x2="1"><stop offset="0" stop-color="#ec5a1c"/><stop offset=".6" stop-color="#f28c1e"/><stop offset="1" stop-color="#ec5a1c"/></linearGradient>
      <linearGradient id="diag-plum" x1="0" x2="1"><stop offset="0" stop-color="#5a2452"/><stop offset=".5" stop-color="#7d2c70"/><stop offset="1" stop-color="#4b2346"/></linearGradient>
    </defs>
    <path d="M0 0 H168 L188 40 L0 104Z" fill="url(#diag-orange)"/>
    <path d="M0 222 L208 150 L258 292 H0Z" fill="url(#diag-orange)"/>
    <path d="M168 0 H521 V48 L208 150Z" fill="url(#diag-plum)"/>
  </svg>
  <div class="wordmark tilted">northvale</div>
  <div class="identity tilted">
    <p class="holder-name">Your Name</p>
    <p class="holder-role">Director</p>
  </div>
  <ul class="contact-list tilted">
    <li><svg class="ico ico-orange"><use href="#i-phone"/></svg>+123-456-789-000</li>
    <li><svg class="ico ico-orange"><use href="#i-mail"/></svg>hello@northvale.com</li>
    <li><svg class="ico ico-orange"><use href="#i-web"/></svg>www.northvale.com</li>
  </ul>
  <p class="address tilted">Address: Cedar Avenue Lindport,<br>Building No.4<br>P.O Box 51920</p>
</section>

<section class="card card-band">
  <svg class="art" width="520" height="289" viewBox="0 0 520 289">
    <defs>
      <linearGradient id="band-plum" x1="0" x2="1"><stop offset="0" stop-color="#4b2346"/><stop offset="1" stop-color="#7d2c70"/></linearGradient>
      <linearGradient id="band-orange" x1="0" x2="1"><stop offset="0" stop-color="#ec5a1c"/><stop offset="1" stop-color="#f28c1e"/></linearGradient>
    </defs>
    <path d="M0 252 H236 L262 272 H520 V289 H0Z" fill="url(#band-plum)"/>
    <path d="M246 252 H520 V266 H262Z" fill="url(#band-orange)"/>
  </svg>
  <div class="identity">
    <p class="holder-name">Your Name</p>
    <p class="holder-role">Position</p>
  </div>
  <ul class="contact-list">
    <li><svg class="ico ico-plum"><use href="#i-mobile"/></svg>123-456-7890</li>
    <li><svg class="ico ico-plum"><use href="#i-phone"/></svg>123-456-7888</li>
    <li><svg class="ico ico-plum"><use href="#i-mail"/></svg>hello@northvale.com</li>
  </ul>
  <div class="wordmark">northvale</div>
  <p class="address">Address: 4170 W. Harbor Lane.<br>Suite 310<br>Dayton, OH 45402</p>
  <p class="site">www.northvale.com</p>
</section>

</body>
</html>
```